Kestrel Motorworks Card

Our company is an offroad fabrication shop that does everything from product installs to complete turnkey offroad racers. We are looking to generate new business cards for the 2014 Lord of the Boulders race in February. This is one of the largest offroad races in the country. We would like to see designs that incorporate the colors used in our logo - black, red, and white.

Industry/Entity Type

Shop

Contact Information for Business Card

KESTREL Motorworks, 2871 Marbury Ln. Houston, TX, 713-542-3097, www.kestrelmotorworks.example, Tom Ellery, Keith Molnar, Owners.

Requirements
Nice to have
• Would like to see the Logo full size on the back size of the car.

```html
<!DOCTYPE html>
<html lang="en">
<head>
<meta charset="utf-8">
<title>Kestrel Motorworks Business Card</title>
<link href="https://fonts.googleapis.com/css2?family=Arimo:ital,wght@0,400;0,700;1,400&display=swap" rel="stylesheet">
<style>
  :root {
    --red: #e3241b;
    --black: #1d1b1b;
    --white: #ffffff;
    --card: #f4f4f4;
    --text: #1e1e1e;
    --bg-center: #ffffff;
    --bg-edge: #dcdcdc;
  }
  * { box-sizing: border-box; margin: 0; padding: 0; }
  html, body { width: 1200px; height: 796px; overflow: hidden; }
  body {
    background: radial-gradient(ellipse at 60% 40%, var(--bg-center) 0%, var(--bg-edge) 100%);
    font-family: "Arimo", Arial, sans-serif;
    position: relative;
  }
  .card {
    position: absolute;
    width: 500px;
    height: 286px;
    background: linear-gradient(135deg, var(--white) 0%, var(--card) 100%);
    box-shadow: 0 6px 18px rgba(0,0,0,0.18);
    overflow: hidden;
  }
  .card-bands { position: absolute; inset: 0; width: 100%; height: 100%; }
  .card-back { left: 110px; top: 140px; }
  .card-front { left: 600px; top: 390px; }

  .back-name {
    position: absolute;
    left: 0; right: 0; top: 118px;
    text-align: center;
    font-weight: 700;
    font-size: 40px;
    color: var(--red);
    letter-spacing: 0.5px;
  }

  .front-title {
    position: absolute;
    left: 30px; top: 38px;
    font-weight: 700;
    font-size: 25px;
    color: var(--red);
  }
  .name-tag {
    position: absolute;
    right: 26px; top: 78px;
    text-align: center;
    color: var(--white);
    width: 160px;
  }
  .name-tag .person { font-weight: 700; font-size: 16px; letter-spacing: 0.5px; }
  .name-tag .role { font-style: italic; font-size: 12px; margin-top: 2px; text-align: right; padding-right: 16px; }

  .contact-list { position: absolute; left: 26px; top: 128px; list-style: none; }
  .contact-item {
    display: flex; align-items: flex-start; gap: 12px;
    font-weight: 700; font-size: 12.5px; color: var(--text);
    line-height: 1.25;
    margin-bottom: 14px;
  }
  .contact-item svg { width: 14px; height: 14px; flex: none; margin-top: 1px; }

  .front-mark {
    position: absolute;
    right: 28px; bottom: 34px;
    display: flex; align-items: center; gap: 8px;
    font-weight: 700; font-size: 17px; color: var(--red);
  }
  .front-mark .dot { width: 12px; height: 12px; background: var(--red); }
</style>
</head>
<body>

  <section class="card card-back" aria-label="Card back">
    <svg class="card-bands" viewBox="0 0 500 286" preserveAspectRatio="none" aria-hidden="true">
      <polygon points="0,0 360,0 352,22 0,22" fill="var(--red)"/>
      <polygon points="368,0 500,0 500,22 360,22" fill="var(--black)"/>
      <polygon points="0,264 180,264 172,286 0,286" fill="var(--black)"/>
      <polygon points="188,264 500,264 500,286 180,286" fill="var(--red)"/>
    </svg>
    <p class="back-name">Kestrel Motorworks</p>
  </section>

  <section class="card card-front" aria-label="Card front">
    <svg class="card-bands" viewBox="0 0 500 286" preserveAspectRatio="none" aria-hidden="true">
      <rect x="0" y="0" width="500" height="14" fill="var(--red)"/>
      <polygon points="300,70 500,70 500,122 282,122" fill="var(--red)"/>
      <polygon points="0,266 200,266 192,286 0,286" fill="var(--black)"/>
      <polygon points="208,266 500,266 500,286 200,286" fill="var(--red)"/>
    </svg>

    <h1 class="front-title">KESTREL Motorworks</h1>

    <div class="name-tag">
      <p class="person">KEITH MOLNAR</p>
      <p class="role">Proprietor</p>
    </div>

    <ul class="contact-list">
      <li class="contact-item">
        <svg viewBox="0 0 14 14" aria-hidden="true"><path d="M7 1a4 4 0 0 0-4 4c0 3 4 8 4 8s4-5 4-8a4 4 0 0 0-4-4zm0 5.5A1.5 1.5 0 1 1 7 3.5a1.5 1.5 0 0 1 0 3z" fill="var(--red)"/></svg>
        <span>2871 Marbury Ln.<br>Houston, TX</span>
      </li>
      <li class="contact-item">
        <svg viewBox="0 0 14 14" aria-hidden="true"><path d="M3.5 1.5l2 2.5-1.2 1.3a7 7 0 0 0 4.4 4.4L10 8.5l2.5 2-1.3 1.8C6.5 12.5 1.5 7.5 1.7 2.8z" fill="var(--red)"/></svg>
        <span>713-542-3097</span>
      </li>
      <li class="contact-item">
        <svg viewBox="0 0 14 14" aria-hidden="true"><circle cx="7" cy="7" r="5.5" fill="none" stroke="var(--red)" stroke-width="1.5"/><path d="M1.5 7h11M7 1.5c-2.5 3-2.5 8 0 11M7 1.5c2.5 3 2.5 8 0 11" fill="none" stroke="var(--red)" stroke-width="1.1"/></svg>
        <span>www.kestrelmotorworks.example</span>
      </li>
    </ul>

    <div class="front-mark">
      <span class="dot" aria-hidden="true"></span>
      <span>Kestrel Motorworks</span>
    </div>
  </section>

</body>
</html>
```